Economics of an Assumption vs Obtaining a New Loan at Current Market Rate

I need to marketing flyer that has fields that calculate mortgage payments amongst other calculations. I have a rough draft that I will attach.

The idea is to provide a tool for a real estate agent to use to illustrate to a potential buyer what a payment would be if they assumed the existing loan on the house or took out a new loan at current market.

The flyer needs to be able to allow an agent to drop in their logo, photo, and contact along with the loan officers photo and contact info.

You can google open house flyer to see examples of what the overall artwork and presentation can look like.

Target Market(s)

Home Buyers

Industry/Entity Type

Real Estate

Colors
F0912C
F2A743
F7CA91
FBE8D2
FDF5EE
EE7325
F08F49
F5BC92
FAE3D3
FDF4ED

Requirements
Must have
• A way to calculate mortgage payment
Nice to have
• Photo and logo drop ins

```html
<!DOCTYPE html>
<html lang="en">
<head>
<meta charset="utf-8">
<title>Havrel Mortgage Comparison Flyer</title>
<link href="https://fonts.googleapis.com/css2?family=Poppins:wght@300;400;500;600;700;800&display=swap" rel="stylesheet">
<style>
  :root{
    --orange:#EE7325;
    --orange-light:#F08F49;
    --black:#0b0b0b;
    --grey-dark:#6b6b6b;
    --grey-pill:#e2e2e2;
    --grey-pill-border:#c9c9c9;
    --grey-card:#c7c7c7;
    --white:#ffffff;
    --ink:#1c1c1c;
  }
  *{box-sizing:border-box;margin:0;padding:0}
  html,body{width:783px;height:1200px;overflow:hidden;background:#fff}
  body{font-family:'Poppins',sans-serif;color:var(--ink)}
  .flyer{position:relative;width:783px;height:1200px;background:var(--white);overflow:hidden}

  .header-art{position:absolute;left:0;top:0}
  .brand{position:absolute;left:70px;top:70px;display:flex;align-items:center;gap:14px}
  .brand-dot{width:26px;height:26px;border-radius:50%;background:var(--orange)}
  .brand-name{font-size:56px;font-weight:300;color:var(--white);letter-spacing:1px;line-height:1}

  .price-label{position:absolute;left:45px;top:256px;line-height:.92;color:var(--black);font-weight:800}
  .price-label .small{font-size:28px;display:block}
  .price-label .big{font-size:48px;display:block;color:var(--white)}
  .price-box{position:absolute;left:211px;top:254px;width:140px;height:72px;background:#fff;border:2px solid #d8d8d8;border-radius:8px}

  .col{position:absolute;top:392px;width:318px}
  .col.left{left:45px}
  .col.right{left:418px}
  .col-title{font-size:17px;font-weight:700;height:26px;display:flex;align-items:center;gap:6px;white-space:nowrap}
  .col-title .accent{color:var(--orange)}
  .badge{display:inline-flex;align-items:center;background:var(--black);border-radius:12px;height:24px;margin-left:4px;overflow:hidden}
  .badge .pct{background:var(--orange);color:#fff;font-weight:800;font-size:19px;padding:0 8px;height:24px;line-height:24px;border-radius:12px}
  .badge .txt{color:#fff;font-size:9px;font-weight:700;padding:0 8px 0 6px}

  .row{position:absolute;left:0;width:318px;height:22px;display:flex;align-items:center;justify-content:space-between;font-size:13.5px}
  .pill{background:var(--grey-pill);border:1px solid var(--grey-pill-border);border-radius:11px;height:22px;font-size:10.5px;color:#444;display:flex;align-items:center;justify-content:center}
  .row .pill{width:170px}
  .total{position:absolute;left:0;width:318px;height:40px;background:var(--orange);border-radius:8px;display:flex;align-items:center;justify-content:space-between;padding:0 6px 0 12px}
  .total span{color:#fff;font-weight:700;font-size:13.5px}
  .total .field{width:162px;height:26px;background:#fff;border-radius:8px}
  .mini{position:absolute;left:0;width:318px;height:22px;display:flex;align-items:center;font-size:13.5px;gap:5px}
  .mini .pill{height:19px;font-size:10px}
  .mini b{font-weight:600}
  .tiny{font-size:9px;line-height:1}

  .diff-bar{position:absolute;left:46px;top:711px;width:690px;height:56px;border-radius:10px;overflow:hidden;display:flex}
  .diff-bar div{display:flex;align-items:center;justify-content:center;font-weight:700;color:#fff}
  .diff-bar .pay{width:345px;background:var(--black);font-size:21px}
  .diff-bar .tot{flex:1;background:var(--grey-dark);font-size:18px}

  .cert-frame{position:absolute;left:41px;top:814px;width:702px;height:244px;border:2px solid #222;border-radius:14px}
  .cert-title{position:absolute;left:0;width:783px;top:792px;text-align:center;font-size:21px;font-weight:400;white-space:nowrap}
  .cert-title span{background:#fff;padding:0 12px}
  .cert-title b{font-weight:800}

  .card{position:absolute;top:841px;height:258px;border-radius:14px;overflow:hidden}
  .card.photo{border:2px solid var(--orange)}
  .card.agent-photo{left:61px;width:157px;background:linear-gradient(160deg,#3b4450 0%,#9aa3ab 45%,#c9b78c 75%,#8d9a86 100%)}
  .card.lender-photo{left:569px;width:157px;background:#efefef}
  .card.contact{width:155px;background:var(--grey-card)}
  .card.contact.a{left:234px}
  .card.contact.b{left:401px}
  .contact-head{height:56px;background:var(--orange);color:#fff;font-weight:700;font-size:15px;line-height:1.15;text-align:center;display:flex;align-items:center;justify-content:center}
  .contact-list{list-style:none;text-align:center;font-size:11.5px;color:#222;padding-top:18px}
  .contact-list li{display:flex;flex-direction:column;align-items:center;gap:4px;height:57px}
  .icon{width:22px;height:22px}

  .site{position:absolute;left:0;width:783px;top:1120px;text-align:center;font-size:24px;letter-spacing:4px;font-weight:400}
  .site b{color:var(--orange);font-weight:700}
  .footer-band{position:absolute;left:0;top:1177px}
</style>
</head>
<body>
<main class="flyer">
  <svg class="header-art" width="783" height="1200" viewBox="0 0 783 1200">
    <rect x="0" y="0" width="783" height="216" fill="var(--black)"/>
    <polygon points="0,216 357,216 424,364 0,364" fill="var(--orange)"/>
    <defs>
      <linearGradient id="houseTones" x1="0" y1="0" x2="0" y2="1">
        <stop offset="0" stop-color="#a9c6e0"/>
        <stop offset="0.35" stop-color="#8d8877"/>
        <stop offset="0.7" stop-color="#b7b1a3"/>
        <stop offset="1" stop-color="#5d8f3a"/>
      </linearGradient>
    </defs>
    <polygon role="img" aria-label="Photo of the property for sale" points="466,0 783,0 783,364 378,364" fill="url(#houseTones)"/>
  </svg>

  <div class="brand">
    <div class="brand-dot"></div>
    <div class="brand-name">Havrel</div>
  </div>

  <div class="price-label"><span class="small">PURCHASE</span><span class="big">PRICE</span></div>
  <div class="price-box"></div>

  <section class="col left">
    <h2 class="col-title">CURRENT <span class="accent">MORTGAGE</span></h2>
    <div class="row" style="top:41px"><span>Loan amount</span><span class="pill">Allow input</span></div>
    <div class="row" style="top:76px"><span>Interest rate</span><span class="pill">Allow input</span></div>
    <div class="row" style="top:112px"><span>Principal &amp; Interest</span><span class="pill">Allow input</span></div>
    <div class="row" style="top:149px"><span>Mortgage Insurance</span><span class="pill">Allow input</span></div>
    <div class="total" style="top:183px"><span>TOTAL</span><div class="field"></div></div>
    <div class="mini" style="top:233px"><span>Years</span><span class="pill" style="width:88px">Input</span><span>Months</span><span class="pill" style="width:92px">Input</span><span class="tiny">Left on<br>loan</span></div>
    <div class="mini" style="top:268px"><b>Tella</b><span class="pill" style="flex:1">Purchase price minus loan amount</span></div>
  </section>

  <section class="col right">
    <h2 class="col-title">NEW <span class="accent">MORTGAGE</span><span class="badge"><span class="pct">10%</span><span class="txt">DOWN PAYMENT</span></span></h2>
    <div class="row" style="top:41px"><span>Loan amount</span><span class="pill">10% of purchase price</span></div>
    <div class="row" style="top:76px"><span>Market rate</span><span class="pill">Input</span></div>
    <div class="row" style="top:112px"><span>Principal &amp; Interest</span><span class="pill">Calc payment</span></div>
    <div class="row" style="top:149px"><span>Mortgage Insurance</span><span class="pill">Input%</span></div>
    <div class="total" style="top:183px"><span>TOTAL</span><div class="field"></div></div>
    <div class="mini" style="top:233px"><span>Term</span><span class="pill" style="width:90px">Input</span><span style="margin-left:auto">Years</span><span class="pill" style="width:88px">Input</span></div>
    <div class="mini" style="top:268px"><b>DOWN payment amount</b><span class="pill" style="flex:1"></span></div>
  </section>

  <div class="diff-bar"><div class="pay">PAYMENT DIFFERENCE</div><div class="tot">DIFFERENCE BETWEEN TOTALS</div></div>

  <div class="cert-frame"></div>
  <h3 class="cert-title"><span>THIS PROPERTY IS <b>"ASSUMABLE LOW RATE VERIFIED"</b></span></h3>

  <div class="card photo agent-photo" role="img" aria-label="Real estate agent photo"></div>

  <div class="card contact a">
    <div class="contact-head">CONTACT<br>INFORMATION</div>
    <ul class="contact-list">
      <li><svg class="icon" viewBox="0 0 22 22"><circle cx="11" cy="11" r="11" fill="#555"/><path d="M7.5 6.2c.6-.5 1.3-.4 1.6.2l.9 1.7c.3.5.1 1-.3 1.3l-.6.4c.5 1.2 1.4 2.1 2.6 2.7l.4-.6c.3-.4.9-.6 1.3-.3l1.7.9c.6.3.7 1 .2 1.6l-.7.8c-.6.6-1.6.7-2.5.3-2.4-1.1-4.2-2.9-5.200-5.3-.4-.9-.2-1.9.4-2.5z" fill="#fff"/></svg>014.582.3907</li>
      <li><svg class="icon" viewBox="0 0 22 22"><circle cx="11" cy="11" r="11" fill="#555"/><rect x="5.5" y="7" width="11" height="8" rx="1" fill="#fff"/><path d="M5.8 7.4 11 11.5l5.2-4.1" fill="none" stroke="#555" stroke-width="1.1"/></svg>info@havrel.com</li>
      <li><svg class="icon" viewBox="0 0 22 22"><circle cx="11" cy="11" r="11" fill="#555"/><g fill="none" stroke="#fff" stroke-width="1.1"><circle cx="11" cy="11" r="5.5"/><ellipse cx="11" cy="11" rx="2.4" ry="5.5"/><path d="M5.5 11h11M6.4 8h9.2M6.4 14h9.2"/></g></svg>www.havrel.com</li>
    </ul>
  </div>

  <div class="card contact b">
    <div class="contact-head">CONTACT<br>INFORMATION</div>
    <ul class="contact-list">
      <li><svg class="icon" viewBox="0 0 22 22"><circle cx="11" cy="11" r="11" fill="#555"/><path d="M7.5 6.2c.6-.5 1.3-.4 1.6.2l.9 1.7c.3.5.1 1-.3 1.3l-.6.4c.5 1.2 1.4 2.1 2.6 2.7l.4-.6c.3-.4.9-.6 1.3-.3l1.7.9c.6.3.7 1 .2 1.6l-.7.8c-.6.6-1.6.7-2.5.3-2.4-1.1-4.2-2.9-5.2-5.3-.4-.9-.2-1.9.4-2.5z" fill="#fff"/></svg>014.582.3907</li>
      <li><svg class="icon" viewBox="0 0 22 22"><circle cx="11" cy="11" r="11" fill="#555"/><rect x="5.5" y="7" width="11" height="8" rx="1" fill="#fff"/><path d="M5.8 7.4 11 11.5l5.2-4.1" fill="none" stroke="#555" stroke-width="1.1"/></svg>info@havrel.com</li>
      <li><svg class="icon" viewBox="0 0 22 22"><circle cx="11" cy="11" r="11" fill="#555"/><g fill="none" stroke="#fff" stroke-width="1.1"><circle cx="11" cy="11" r="5.5"/><ellipse cx="11" cy="11" rx="2.4" ry="5.5"/><path d="M5.5 11h11M6.4 8h9.2M6.4 14h9.2"/></g></svg>www.havrel.com</li>
    </ul>
  </div>

  <div class="card photo lender-photo" role="img" aria-label="Loan officer photo or logo"></div>

  <p class="site">www.<b>havrel</b>.com</p>

  <svg class="footer-band" width="783" height="23" viewBox="0 0 783 23" aria-hidden="true">
    <polygon points="0,0 404,0 390,23 0,23" fill="var(--black)"/>
    <polygon points="404,0 783,0 783,23 390,23" fill="var(--orange)"/>
  </svg>
</main>
</body>
</html>
```